Plakat-Design für IT-Firma
Zielgruppe
Wir sind eine junge dynamische B2B IT Firma, die für ihre Kunden (kleine & mittelständische Unternehmen) einen Full-Service (Server, Computer, Telefonanlagen) bietet. Wir kümmern uns um alles, was einen Stecker hat.
Aufgabenstellung
Wir benötigen eine Datei für eine Plakatwerbung, die auf großen LED Screens am Straßenrand zu sehen sein wird (Seitenverhältnis 672 ×432). Außerdem möchten wir diese auch als PDF veröffentlichen.
Wir möchten, dass unser Logo zusehen ist sowie folgender Text:
'Sie sorgen für die Abläufe im Unternehmen.
Wir für die reibungslose IT.
kolvanda-tec.de'
Die Farben sollten Blau, Orange und Grau sein, wie auf unserer Webseite kolvanda-tec.de zu sehen ist.
Wir sind offen, für kreative Ideen, auch leichte Abänderungen der Wortlaute können wir uns vorstellen.
Es ist wichtig, dass es kurz und prägnant ist. Dass es an der roten Ampelphase, beim kurzen Vorbeifahren in Erinnerung bleibt, optisch Aufmerksamkeit erregt und neugierig macht.
Wir benötigen folgende Formate:
1. JPG Datei in 672 ×432
2. Bilddatei in mind. Full HD
3. PDF

```html
<!DOCTYPE html>
<html lang="de">
<head>
<meta charset="utf-8">
<title>kolvandatec – Plakat</title>
<link rel="stylesheet" href="https://fonts.googleapis.com/css2?family=Inter:wght@400;700;800&display=swap">
<style>
  :root {
    --page: #e9e8e4;
    --night-blue: #0c1b2e;
    --steel-blue: #2c4a6b;
    --glow-blue: #5d86b0;
    --orange: #e06a3e;
    --white: #ffffff;
    --grey-text: #3d4650;
  }
  * { box-sizing: border-box; margin: 0; padding: 0; }
  html, body { width: 1200px; height: 987px; overflow: hidden; }
  body {
    background: var(--page);
    font-family: "Inter", Arial, sans-serif;
    position: relative;
  }
  .poster {
    position: absolute;
    left: 40px;
    top: 133px;
    width: 1120px;
    height: 720px;
    overflow: hidden;
    background: var(--night-blue);
  }
  .poster-photo {
    position: absolute;
    inset: 0;
    background:
      radial-gradient(ellipse at 78% 45%, rgba(160,185,210,0.55) 0%, rgba(160,185,210,0) 38%),
      radial-gradient(ellipse at 40% 60%, rgba(93,134,176,0.55) 0%, rgba(93,134,176,0) 55%),
      linear-gradient(180deg, var(--steel-blue) 0%, var(--night-blue) 100%);
  }
  .headline {
    position: absolute;
    left: 71px;
    top: 78px;
    color: var(--white);
    font-weight: 700;
    font-size: 58px;
    line-height: 71px;
    letter-spacing: -0.3px;
  }
  .claim-band {
    position: absolute;
    left: 0;
    top: 425px;
    width: 820px;
    height: 263px;
    background: linear-gradient(90deg, var(--orange) 0%, var(--orange) 76%, rgba(224,106,62,0.55) 90%, rgba(224,106,62,0) 100%);
  }
  .claim {
    position: absolute;
    left: 68px;
    top: 442px;
    color: var(--white);
    font-weight: 700;
    font-size: 58px;
    line-height: 71px;
    letter-spacing: -0.3px;
  }
  .web-address {
    position: absolute;
    left: 69px;
    top: 610px;
    color: var(--white);
    font-weight: 400;
    font-size: 38px;
  }
  .brand-panel {
    position: absolute;
    right: 0;
    top: 612px;
    width: 416px;
    height: 76px;
    background: var(--white);
  }
  .footer-strip {
    position: absolute;
    left: 0;
    bottom: 0;
    width: 100%;
    height: 32px;
    background: var(--white);
  }
  .brand-name {
    position: absolute;
    right: 48px;
    top: 650px;
    color: var(--grey-text);
    font-weight: 700;
    font-size: 34px;
    letter-spacing: 1px;
    text-transform: uppercase;
  }
  .brand-tagline {
    position: absolute;
    right: 48px;
    top: 694px;
    color: var(--grey-text);
    font-weight: 400;
    font-size: 12px;
    letter-spacing: 0.5px;
    text-transform: uppercase;
  }
</style>
</head>
<body>
  <main class="poster">
    <div class="poster-photo" role="img" aria-label="Foto: IT-Fachmann mit Tablet in einem beleuchteten Serverraum"></div>
    <h1 class="headline">Sie sorgen für<br>die Abläufe im<br>Unternehmen.</h1>
    <div class="claim-band"></div>
    <p class="claim">Wir für die<br>reibungslose IT.</p>
    <p class="web-address">www.kolvanda-tec.de</p>
    <div class="brand-panel"></div>
    <div class="footer-strip"></div>
    <p class="brand-name">kolvandatec</p>
    <p class="brand-tagline">IT-Sicherheit Datensicherheit Datenschutz</p>
  </main>
</body>
</html>
```